Business Card Design Project

This is to go hand in hand with our stationery project.
Target Market(s)
Business Professionals in the Finance, HR and C-Level management arena. They are global companies that run enterprise technology solutions/products.
Mostly Male, mid 30's to 60's.
Industry/Entity Type
Business
Font styles to use
Other font styles liked:
- Calibri
Colors
9bcb3c
000000
1b1b1b
c4c4c4
ffffff
Requirements
Must have
- Logo
Name, title, contact details, address on the front of the card.
ABN and web address need to be on the card, along with our tag line
Think | Link | Act
We also require rounded corners and for the card to be landscape please.
Our green is
C98 M0 Y93 K0
Modern, contemporary and must have white space for people to write on.
Nice to have
- Consistent elements with the stationery design.
Should not have
- No 90's waves - We want the feeling of movement but no wavey lines.

```html
<!DOCTYPE html>
<html lang="en">
<head>
<meta charset="utf-8">
<title>Orvex Business Solutions – Business Card</title>
<link rel="stylesheet" href="https://fonts.googleapis.com/css2?family=Open+Sans:wght@400;600;700&display=swap">
<style>
  :root {
    --lime: #84fb04;
    --ink: #1b1b1b;
    --paper: #ffffff;
    --stage-light: #8a8c8d;
    --stage-dark: #2a2b2c;
    --label: #f2f2f2;
    --ghost: rgba(255, 255, 255, 0.22);
  }
  * { box-sizing: border-box; margin: 0; padding: 0; }
  html, body { width: 1200px; height: 750px; overflow: hidden; }
  body {
    font-family: "Open Sans", sans-serif;
    background: radial-gradient(ellipse at 35% 25%, var(--stage-dark) 0%, #4a4b4c 55%, var(--stage-light) 100%);
    position: relative;
  }
  .card {
    position: absolute;
    top: 210px;
    width: 560px;
    height: 320px;
    background: var(--paper);
    border-radius: 6px;
    padding: 9px;
  }
  .card--front { left: 30px; }
  .card--back { left: 610px; }
  .card__face {
    position: relative;
    width: 100%;
    height: 100%;
    background: var(--lime);
    border-radius: 9px;
    overflow: hidden;
  }
  .side-label {
    position: absolute;
    top: 552px;
    width: 560px;
    text-align: center;
    color: var(--label);
    font-size: 22px;
    font-weight: 600;
    letter-spacing: 1px;
  }
  .side-label--front { left: 30px; }
  .side-label--back { left: 610px; }

  /* faint background emblem */
  .ghost-mark {
    position: absolute;
    width: 240px;
    height: 200px;
    border-radius: 16px;
    background: var(--ghost);
    transform: rotate(40deg);
    display: flex;
    align-items: center;
    justify-content: center;
  }
  .ghost-mark__name {
    color: rgba(255, 255, 255, 0.35);
    font-weight: 600;
    font-size: 48px;
  }
  .card--front .ghost-mark { left: 20px; top: 120px; }
  .card--back .ghost-mark { left: -10px; top: 40px; }

  /* logo lockup */
  .brand {
    position: absolute;
    display: flex;
    align-items: center;
    gap: 10px;
    color: var(--ink);
    font-weight: 700;
  }
  .brand__square {
    width: 34px;
    height: 34px;
    background: var(--ink);
    border-radius: 4px;
    flex: none;
  }
  .brand__text { line-height: 1.05; }
  .brand__name { display: block; font-size: 36px; }
  .brand__sub { display: block; font-size: 14px; }
  .card--front .brand { left: 60px; top: 22px; }
  .card--back .brand { right: 40px; top: 100px; }

  /* contact block */
  .contact {
    position: absolute;
    right: 20px;
    top: 10px;
    width: 250px;
    text-align: right;
    color: var(--paper);
  }
  .contact__name { font-size: 28px; font-weight: 600; line-height: 1.25; }
  .contact__rule { height: 1px; background: var(--paper); margin: 3px 0 2px; }
  .contact__line { font-size: 15px; line-height: 1.35; }

  .sign-off {
    position: absolute;
    right: 28px;
    bottom: 14px;
    text-align: center;
    color: var(--ink);
    font-weight: 700;
    font-size: 15px;
    line-height: 1.5;
  }
</style>
</head>
<body>
  <section class="card card--front" aria-label="Card front">
    <div class="card__face">
      <div class="ghost-mark" aria-hidden="true"><span class="ghost-mark__name">Orvex</span></div>
      <div class="brand">
        <span class="brand__square"></span>
        <span class="brand__text">
          <span class="brand__name">Orvex</span>
          <span class="brand__sub">Business Solutions</span>
        </span>
      </div>
      <div class="contact">
        <p class="contact__name">Liam Carter</p>
        <div class="contact__rule"></div>
        <p class="contact__line">HR Head</p>
        <p class="contact__line">9845550172</p>
        <p class="contact__line">Harbourview, Australia</p>
      </div>
      <div class="sign-off">
        <p>Think | Link | Act</p>
        <p>www.orvexbusiness.com</p>
      </div>
    </div>
  </section>
  <p class="side-label side-label--front">FRONT</p>

  <section class="card card--back" aria-label="Card back">
    <div class="card__face">
      <div class="ghost-mark" aria-hidden="true"><span class="ghost-mark__name">Orvex</span></div>
      <div class="brand">
        <span class="brand__square"></span>
        <span class="brand__text">
          <span class="brand__name">Orvex</span>
          <span class="brand__sub">Business Solutions</span>
        </span>
      </div>
    </div>
  </section>
  <p class="side-label side-label--back">BACK</p>
</body>
</html>
```